Website for new slot-booking/reservations website/software

For a new software product we need a brand new logo and website for a reservations/booking system. The website should ideally present the main features with information text, contact info, news page as well as registration and pricing pages. As currently primary field of operation the software should be used for tennis but later on, also for other sport types. Also we'd like to be the logo a text-brand which includes the name "feldreserva.net" or just "feldreserva". The logo should ideally include an icon-design in some way. Generally we are open for ideas.

Bootstrap 4 template is a minimum requirement. (Multi-Page preferred, Single-Page still OK.)

You can use the attached image as an inspiration, but change of colors or other design elements are up to you. Currently the application has a primary color of #5500ff. The website created by you will not include the application itself, so it can have different (but ideally similar) Look&Feel.

Target Market(s)

Sports, Club-Management

Logo Text

feldreserva.net

Coding

Coded - Design and coding required

Number of Pages Required

5+ page

Font styles to use
Sans Serif

Requirements
Must have
• Bootstrap 4 Template, SCSS
Nice to have
• Rapid Loading Times, not too much external JS Libraries.
Should not have
• Extensive animations

```html
<!DOCTYPE html>
<html lang="en">
<head>
<meta charset="utf-8">
<title>feldreserva – Court Reservations</title>
<link rel="stylesheet" href="https://fonts.googleapis.com/css2?family=Josefin+Sans:wght@300;400;600;700&display=swap">
<style>
:root{
  --primary:#5500ff;
  --accent:#efe461;
  --ink:#1c1c1c;
  --muted:#8a8a8a;
  --band:#f0f0f0;
  --soft:#f8f8f8;
  --footer:#050505;
  --white:#ffffff;
}
*{margin:0;padding:0;box-sizing:border-box}
html,body{width:1200px;height:4843px;overflow:hidden}
body{position:relative;background:var(--white);font-family:"Josefin Sans",sans-serif;color:var(--ink)}
.abs{position:absolute}
.photo{position:absolute}
/* nav */
.site-nav{position:absolute;left:0;top:0;width:1200px;height:64px;background:var(--white);z-index:2}
.brand{position:absolute;left:182px;top:14px;font-size:27px;font-weight:700;color:var(--primary)}
.menu a{position:absolute;top:24px;font-size:14px;color:var(--ink);text-decoration:none}
.menu a.active{color:var(--primary)}
.menu a.active::after{content:"";position:absolute;left:50%;top:24px;width:14px;height:2px;margin-left:-7px;background:var(--primary)}
/* buttons */
.btn{position:absolute;display:flex;align-items:center;justify-content:center;font-size:14px;border-radius:4px;text-decoration:none}
.btn-primary{background:var(--primary);color:var(--white)}
.btn-accent{background:var(--accent);color:var(--ink)}
/* hero */
.hero-photo{left:0;top:64px;width:1200px;height:536px;background:linear-gradient(100deg,#4a2a24 0%,#7a3f30 35%,#8d4a36 55%,#3e3a2a 100%)}
.hero-title{left:182px;top:178px;font-size:48px;line-height:55px;font-weight:400;color:var(--white)}
.hero-text{left:182px;top:318px;width:410px;font-size:12px;line-height:25px;color:var(--white)}
.dots span{position:absolute;top:541px;width:6px;height:6px;border-radius:50%;background:var(--white)}
.dots span.on{background:var(--primary)}
/* section type */
.eyebrow{position:absolute;font-size:13px;color:var(--primary)}
.heading{position:absolute;font-size:34px;line-height:47px;font-weight:400;color:var(--ink)}
.copy{position:absolute;font-size:12px;line-height:24.5px;color:var(--muted)}
.copy b{color:var(--ink);font-weight:600}
/* contact */
.contact-band{left:0;top:2385px;width:1200px;height:311px;background:var(--band)}
.contact-row{position:absolute;left:610px;display:flex;align-items:center;gap:18px;font-size:17px;color:#555}
.icon-ring{width:44px;height:44px;border-radius:50%;border:2px solid var(--accent);display:flex;align-items:center;justify-content:center}
/* news */
.date-badge{left:833px;top:3008px;width:183px;height:58px;background:var(--primary);color:var(--white);font-size:17px;display:flex;align-items:center;justify-content:center;border-radius:4px}
.news-title{font-size:17px;line-height:25px}
.link{position:absolute;font-size:13px;color:var(--primary)}
.news-item .date{position:absolute;font-size:9px;color:var(--muted)}
.news-item .text{position:absolute;width:250px;font-size:13px;line-height:23px;color:var(--ink)}
/* testimonial */
.testi-bg{left:0;top:3551px;width:730px;height:713px;background:var(--soft)}
.quote-badge{left:560px;top:3859px;width:80px;height:80px;border-radius:50%;background:var(--primary);z-index:1;display:flex;align-items:center;justify-content:center;color:var(--white);font-size:46px;font-weight:700;line-height:1}
.arrow{position:absolute;width:46px;height:46px;border-radius:50%;display:flex;align-items:center;justify-content:center}
.quote-text{position:absolute;left:182px;width:370px;font-size:12px;line-height:24.5px;color:var(--ink)}
/* footer */
.site-footer{left:0;top:4460px;width:1200px;height:383px;background:var(--footer);color:var(--white)}
.footer-brand{left:182px;top:4540px;font-size:27px;font-weight:700;color:var(--white)}
.footer-head{position:absolute;top:4550px;font-size:14px;font-weight:400;color:var(--white)}
.footer-info{position:absolute;left:182px;display:flex;gap:22px;font-size:11px;line-height:17px;color:#ddd}
.footer-link{position:absolute;font-size:12px;color:#ddd}
.subscribe{left:786px;top:4599px;width:230px;height:40px;background:var(--white);border-radius:4px;border:2px solid var(--accent)}
.subscribe span{position:absolute;left:20px;top:13px;font-size:10px;color:#aaa}
.subscribe b{position:absolute;right:4px;top:4px;width:62px;height:28px;background:var(--accent);border-radius:4px;font-size:11px;font-weight:400;color:var(--ink);display:flex;align-items:center;justify-content:center}
.social{position:absolute;top:4672px;width:14px;height:14px;border-radius:50%;background:var(--white)}
.footer-rule{left:182px;top:4765px;width:834px;height:1px;background:#2a2a2a}
.copyright{left:0;top:4784px;width:1200px;text-align:center;font-size:12px;color:#ddd}
</style>
</head>
<body>

<header class="site-nav">
  <div class="brand">feldreserva</div>
  <nav class="menu">
    <a class="active" style="left:557px">Home</a>
    <a style="left:643px">About Us</a>
    <a style="left:754px">Reservation</a>
    <a style="left:880px">Contact</a>
    <a style="left:981px">News</a>
    <a style="left:1064px">Sign-Up</a>
  </nav>
</header>

<section class="hero">
  <div class="photo hero-photo" role="img" aria-label="Close-up of a tennis ball resting on a racket on a clay court"></div>
  <h1 class="abs hero-title">Match Of The Year<br>Is Coming</h1>
  <p class="abs hero-text">Lorem ipsum dolor sit amet, consectetur adipiscing elit, sed do eiusmod tempor incididunt ut labore et dolore magna aliqua. Quis ipsum suspendisse ultrices gravida.</p>
  <a class="btn btn-primary" style="left:182px;top:427px;width:140px;height:51px">Learn More</a>
  <a class="btn btn-accent" style="left:346px;top:427px;width:128px;height:51px">Book Now</a>
  <div class="dots"><span style="left:183px"></span><span class="on" style="left:198px"></span><span style="left:213px"></span><span style="left:227px"></span></div>
</section>

<section class="about">
  <p class="eyebrow" style="left:182px;top:689px">....About Us</p>
  <h2 class="heading" style="left:182px;top:724px;width:350px">feldreserva is the<br>most advanced sports<br>trading &amp; highest<br>stakes across multiple<br>bookmakers and<br>exchanges.</h2>
  <p class="copy" style="left:611px;top:725px;width:405px">Duis aute irure dolor in reprehenderit in voluptate velit esse cillum dolore eu fugiat nulla pariatur. Excepteur sint occaecat cupidatat non proident, sunt in culpa qui officia deserunt mollit anim id est laborum. Sed ut perspiciatis unde omnis iste natus error sit <b>voluptatem, accusantium, doloremque, laudantium,</b> totam rem aperiam, eaque ipsa quae ab illo inventore veritatis et quasi architecto beatae vitae dicta sunt explicabo.</p>
  <p class="copy" style="left:611px;top:925px;width:405px">Nemo enim ipsam voluptatem quia voluptas sit aspernatur aut odit aut fugit, sed quia consequuntur magni dolores eos qui ratione voluptatem sequi nesciunt.</p>
  <a class="btn btn-accent" style="left:611px;top:1036px;width:134px;height:51px">Read More</a>
</section>

<section class="gallery">
  <div class="photo" style="left:0;top:1179px;width:265px;height:333px;background:linear-gradient(160deg,#e7b86a,#6d6a5a 60%,#4b5560)" role="img" aria-label="Player serving at sunset on an outdoor court"></div>
  <div class="photo" style="left:267px;top:1179px;width:331px;height:333px;background:linear-gradient(170deg,#c7764e,#d48a63 60%,#c46e48)" role="img" aria-label="Player holding a racket on a clay court"></div>
  <div class="photo" style="left:600px;top:1179px;width:331px;height:333px;background:linear-gradient(170deg,#8aa07a,#b8b8a8 50%,#6d6f70)" role="img" aria-label="Player preparing to hit a ball"></div>
  <div class="photo" style="left:933px;top:1179px;width:267px;height:333px;background:linear-gradient(170deg,#c97a55,#d08b66 60%,#b96a45)" role="img" aria-label="Racket and ball beside a player's shoes on clay"></div>
</section>

<section class="reservation">
  <p class="eyebrow" style="left:182px;top:1799px">....Reservation</p>
  <h2 class="heading" style="left:182px;top:1832px;width:400px">Nemo enim ipsam quia voluptas sit aspernatur aut odit aut fugit.</h2>
  <p class="copy" style="left:182px;top:2003px;width:370px">Neque porro quisquam est, qui dolorem ipsum quia dolor sit amet, consectetur, adipisci velit, sed quia non numquam eius modi tempora incidunt ut labore et dolore magnam aliquam quaerat voluptatem.</p>
  <a class="btn btn-accent" style="left:182px;top:2139px;width:130px;height:51px">Book Now</a>
  <div class="photo" style="left:611px;top:1603px;width:589px;height:587px;background:linear-gradient(160deg,#f4b49a,#f1a98d 60%,#e9a184)" role="img" aria-label="Smiling tennis player holding a racket over her shoulder"></div>
</section>

<section class="contact">
  <div class="abs contact-band"></div>
  <div class="photo" style="left:207px;top:2272px;width:278px;height:424px;background:linear-gradient(180deg,#e6e6e6,#dcdcdc 50%,#c9c9c9)" role="img" aria-label="Goalkeeper in a white and orange kit holding gloves"></div>
  <p class="eyebrow" style="left:610px;top:2429px">....Conatct</p>
  <h2 class="heading" style="left:610px;top:2468px">Feel free to contact</h2>
  <div class="contact-row" style="top:2542px">
    <span class="icon-ring"><svg width="16" height="16" viewBox="0 0 24 24"><path fill="#111" d="M6.6 10.8a15.1 15.1 0 0 0 6.6 6.6l2.2-2.2c.3-.3.7-.4 1-.2 1.1.4 2.3.6 3.6.6.6 0 1 .4 1 1V20c0 .6-.4 1-1 1A17 17 0 0 1 3 4c0-.6.4-1 1-1h3.5c.6 0 1 .4 1 1 0 1.3.2 2.5.6 3.6.1.3 0 .7-.2 1z"/></svg></span>
    +14 3600 555 018
  </div>
  <div class="contact-row" style="top:2606px">
    <span class="icon-ring"><svg width="16" height="14" viewBox="0 0 24 20"><rect x="1" y="2" width="22" height="16" rx="1" fill="#111"/><path d="M2 3l10 8 10-8" stroke="#fff" stroke-width="2" fill="none"/></svg></span>
    feldreserva@gmail.com
  </div>
</section>

<section class="news">
  <p class="eyebrow" style="left:182px;top:2920px">....News</p>
  <h2 class="heading" style="left:182px;top:2955px;width:340px">Here you can find sports related every recent news.</h2>
  <p class="copy" style="left:182px;top:3122px;width:320px">Duis aute irure dolor in reprehenderit in voluptate velit esse cillum dolore eu fugiat nulla pariatur. Excepteur sint occaecat cupidatat.</p>
  <a class="btn btn-accent" style="left:182px;top:3234px;width:134px;height:51px">View More</a>

  <div class="photo" style="left:611px;top:2786px;width:405px;height:252px;background:linear-gradient(160deg,#b8c4d0,#8a8f95 45%,#6d8f4e 80%)" role="img" aria-label="Football hitting the net of a goal in a stadium"></div>
  <div class="abs date-badge">15 April, 2021</div>
  <h3 class="abs news-title" style="left:611px;top:3106px;width:410px;font-weight:400">Lorem ipsum dolor sit amet, consectetur adipiscing elit, sed do eiusmod tempor incididunt</h3>
  <p class="copy" style="left:611px;top:3160px;width:400px">Lorem ipsum dolor sit amet, consectetur adipiscing elit, sed do eiusmod tempor incididunt ut labore et dolore magna aliqua. Quis ipsum suspendisse ultrices gravida. Risus commodo viverra maecenas accumsan lacus vel facilisis.</p>
  <a class="link" style="left:611px;top:3274px">Continue Reading...</a>

  <article class="news-item">
    <div class="photo" style="left:182px;top:3352px;width:123px;height:111px;background:linear-gradient(160deg,#5f8a55,#9b4f3f 60%,#b05a45)" role="img" aria-label="Runners on a red athletics track"></div>
    <span class="date" style="left:325px;top:3358px">11 April,2021</span>
    <p class="text" style="left:325px;top:3376px">Ut enim ad minim veniam, quis nostrud exercitation ullamco laboris nisi ut aliquip ex ea commodo.</p>
  </article>
  <article class="news-item">
    <div class="photo" style="left:611px;top:3352px;width:121px;height:111px;background:linear-gradient(160deg,#c98a5a,#a86a48 60%,#6a6a5a)" role="img" aria-label="Golfer finishing a swing on a course"></div>
    <span class="date" style="left:752px;top:3358px">06 April,2021</span>
    <p class="text" style="left:752px;top:3376px">Ut enim ad minim veniam, quis nostrud exercitation ullamco laboris nisi ut aliquip ex ea commodo.</p>
  </article>
</section>

<section class="testimonial">
  <div class="abs testi-bg"></div>
  <p class="eyebrow" style="left:182px;top:3642px">....Testimonial</p>
  <h2 class="heading" style="left:182px;top:3678px">What our clients say about us.</h2>
  <p class="copy" style="left:182px;top:3750px;width:540px">Duis aute irure dolor in reprehenderit in voluptate velit esse cillum dolore eu fugiat nulla pariatur. Excepteur sint occaecat cupidatat non proident, sunt in culpa qui officia deserunt mollit anim id est laborum.</p>
  <div class="photo" style="left:589px;top:3899px;width:427px;height:471px;background:linear-gradient(160deg,#b7a27a,#8d7a55 50%,#5f5a44)" role="img" aria-label="Portrait of a smiling client outdoors"></div>
  <div class="abs quote-badge">&#8221;</div>
  <p class="quote-text" style="top:3992px">Lorem ipsum dolor sit amet, consectetur adipiscing elit, sed do eiusmod tempor incididunt ut labore et dolore magna aliqua. Ut enim ad minim veniam, quis nostrud exercitation ullamco laboris nisi ut aliquip ex ea commodo consequat.</p>
  <p class="quote-text" style="top:4117px">Duis aute irure dolor in reprehenderit in voluptate velit esse cillum dolore eu fugiat nulla pariatur.</p>
  <p class="abs" style="left:371px;top:4190px;font-size:13px">_Clara Weston</p>
  <span class="arrow" style="left:99px;top:4112px;background:#e3e3e3"><svg width="10" height="14" viewBox="0 0 10 14"><path d="M7 2L2 7l5 5" stroke="#777" stroke-width="1.6" fill="none"/></svg></span>
  <span class="arrow" style="left:1053px;top:4112px;background:var(--accent)"><svg width="10" height="14" viewBox="0 0 10 14"><path d="M3 2l5 5-5 5" stroke="#111" stroke-width="1.8" fill="none"/></svg></span>
</section>

<footer class="abs site-footer"></footer>
<div class="abs footer-brand">feldreserva</div>
<div class="footer-info" style="top:4603px"><svg width="12" height="16" viewBox="0 0 12 16"><path fill="#fff" d="M6 0a6 6 0 0 0-6 6c0 4.5 6 10 6 10s6-5.5 6-10a6 6 0 0 0-6-6zm0 8.2A2.2 2.2 0 1 1 6 3.8a2.2 2.2 0 0 1 0 4.4z"/></svg><span>Lorem ipsum dolor<br>sit amet, psum primis.</span></div>
<div class="footer-info" style="top:4657px"><svg width="13" height="13" viewBox="0 0 24 24"><path fill="#fff" d="M6.6 10.8a15.1 15.1 0 0 0 6.6 6.6l2.2-2.2c.3-.3.7-.4 1-.2 1.1.4 2.3.6 3.6.6.6 0 1 .4 1 1V20c0 .6-.4 1-1 1A17 17 0 0 1 3 4c0-.6.4-1 1-1h3.5c.6 0 1 .4 1 1 0 1.3.2 2.5.6 3.6.1.3 0 .7-.2 1z"/></svg><span>(+91) 555 - 010 - 321</span></div>
<div class="footer-info" style="top:4692px"><svg width="14" height="12" viewBox="0 0 24 20"><rect x="1" y="2" width="22" height="16" rx="1" fill="#fff"/><path d="M2 3l10 8 10-8" stroke="#000" stroke-width="2" fill="none"/></svg><span>hello@feldreserva.net</span></div>

<h4 class="footer-head" style="left:448px">Quick Links</h4>
<a class="footer-link" style="left:448px;top:4606px">Home</a>
<a class="footer-link" style="left:448px;top:4642px">About us</a>
<a class="footer-link" style="left:448px;top:4680px">Reservation</a>
<a class="footer-link" style="left:448px;top:4715px">Contact</a>
<a class="footer-link" style="left:589px;top:4606px">News</a>
<a class="footer-link" style="left:589px;top:4642px">Testimonial</a>
<a class="footer-link" style="left:589px;top:4680px">Trams &amp; Condition</a>
<a class="footer-link" style="left:589px;top:4715px">Privacy &amp; Policy</a>

<h4 class="footer-head" style="left:786px">Subscribe</h4>
<div class="abs subscribe"><span>Enter Your Email</span><b>Join</b></div>
<span class="social" style="left:790px"></span>
<span class="social" style="left:830px"></span>
<span class="social" style="left:868px"></span>
<span class="social" style="left:907px"></span>

<div class="abs footer-rule"></div>
<p class="abs copyright">copyright@ 2021 feldreserva.net</p>

</body>
</html>
```